Supplement Company Needs a Protein Powder Pouch Design

We are looking for a modern and fresh design for our 500g pouches of protein powder as our current design is not eye catching or exciting enough.

This new design will be printed on both sides of a 178mm x 280mm x 101mm pouch.

We have 4 flavours. These are Banana Ice Cream, Chocolate Deluxe, Strawberries & Cream and Vanilla Ice Cream.

Industry/Entity Type

Supplement

Requirements
Must have
• Attractive and eye catching front and space for all the nutritional information and ingredients on the back.

Must clearly state 'food supplement' somewhere on the front of the pouch.
Nice to have
• Our logo is attached.
Should not have
• No health claims as these are not allowed in the UK

```html
<!DOCTYPE html>
<html lang="en">
<head>
<meta charset="utf-8">
<title>ZEST Supplements – Protein Powder Pouch Range</title>
<link href="https://fonts.googleapis.com/css2?family=Jost:wght@500&family=Montserrat:wght@700&display=swap" rel="stylesheet">
<style>
  :root {
    --stage: #e9e9e9;
    --pouch-dark: #0c0c0c;
    --pouch-mid: #1e1e1e;
    --seal: #262626;
    --white: #ffffff;
    --ink: #0a0a0a;
    --halo-top: #d9d9d9;
    --halo-bottom: #8c8c8c;
    --banana: #ffd400;
    --chocolate: #9a3a05;
    --strawberry: #ee1c24;
    --vanilla: #ffdc9a;
  }
  * { box-sizing: border-box; margin: 0; padding: 0; }
  html, body { width: 1200px; height: 720px; overflow: hidden; }
  body {
    background: var(--stage);
    font-family: "Montserrat", Arial, sans-serif;
    position: relative;
  }
  .range { position: absolute; inset: 0; }
  .pouch {
    position: absolute;
    top: 196px;
    width: 258px;
    height: 408px;
    background: var(--pouch-dark);
    overflow: hidden;
    color: var(--white);
  }
  .pouch--banana { left: 69px; --flavour: var(--banana); }
  .pouch--chocolate { left: 339px; --flavour: var(--chocolate); }
  .pouch--strawberry { left: 608px; --flavour: var(--strawberry); }
  .pouch--vanilla { left: 878px; --flavour: var(--vanilla); }

  .pouch__pattern {
    position: absolute; inset: 0;
    background: radial-gradient(ellipse at 50% 45%, var(--pouch-mid) 0%, var(--pouch-dark) 75%);
  }
  .pouch__seal {
    position: absolute; left: 0; right: 0; top: 0; height: 20px;
    background: var(--seal);
  }
  .pouch__tear {
    position: absolute; left: 8px; right: 8px; top: 31px;
    border-top: 1px dashed rgba(255,255,255,0.45);
  }
  .brand {
    position: absolute; left: 0; right: 0; top: 80px;
    text-align: center;
    font-weight: 700; font-size: 18px; line-height: 1; letter-spacing: 2px;
    color: var(--white);
  }
  .halo {
    position: absolute; left: 60px; top: 131px;
    width: 138px; height: 69px;
    border-radius: 69px 69px 0 0;
    background: linear-gradient(180deg, var(--halo-top) 0%, var(--halo-bottom) 100%);
  }
  .category {
    position: absolute; left: 0; right: 0; top: 154px;
    text-align: center;
    font-weight: 700; font-size: 7px; letter-spacing: 0.9px;
    color: var(--ink);
  }
  .title-pill {
    position: absolute; left: 27px; top: 176px;
    width: 204px; height: 35px; border-radius: 18px;
    background: var(--flavour);
  }
  .title {
    position: absolute; left: 0; right: 0;
    text-align: center;
    font-family: "Jost", "Futura", sans-serif; font-weight: 500;
    font-size: 33px; line-height: 1; letter-spacing: 3.5px;
  }
  .title--top { top: 177px; color: var(--ink); }
  .title--bottom { top: 213px; color: var(--flavour); }
  .flavour {
    position: absolute; left: 0; right: 0; top: 291px;
    text-align: center;
    font-weight: 700; font-size: 8.5px; letter-spacing: 2.6px;
  }
  .flavour-dot {
    position: absolute; left: 120px; top: 310px;
    width: 19px; height: 19px; border-radius: 50%;
    background: var(--flavour);
  }
  .weight {
    position: absolute; left: 0; right: 0; top: 368px;
    text-align: center;
    font-weight: 700; font-size: 14px; letter-spacing: 1.2px;
  }
</style>
</head>
<body>
<main class="range">

  <article class="pouch pouch--banana">
    <div class="pouch__pattern" role="img" aria-label="Black pouch face with fine radiating line pattern"></div>
    <div class="pouch__seal"></div>
    <div class="pouch__tear"></div>
    <p class="brand">ZEST SUPPLEMENTS</p>
    <div class="halo"></div>
    <p class="category">• FOOD SUPPLEMENT •</p>
    <div class="title-pill"></div>
    <h2 class="title title--top">PROTEIN</h2>
    <p class="title title--bottom">POWDER</p>
    <p class="flavour">BANANA ICE CREAM</p>
    <div class="flavour-dot"></div>
    <p class="weight">500G</p>
  </article>

  <article class="pouch pouch--chocolate">
    <div class="pouch__pattern" role="img" aria-label="Black pouch face with fine radiating line pattern"></div>
    <div class="pouch__seal"></div>
    <div class="pouch__tear"></div>
    <p class="brand">ZEST SUPPLEMENTS</p>
    <div class="halo"></div>
    <p class="category">• FOOD SUPPLEMENT •</p>
    <div class="title-pill"></div>
    <h2 class="title title--top">PROTEIN</h2>
    <p class="title title--bottom">POWDER</p>
    <p class="flavour">CHOCOLATE DELUXE</p>
    <div class="flavour-dot"></div>
    <p class="weight">500G</p>
  </article>

  <article class="pouch pouch--strawberry">
    <div class="pouch__pattern" role="img" aria-label="Black pouch face with fine radiating line pattern"></div>
    <div class="pouch__seal"></div>
    <div class="pouch__tear"></div>
    <p class="brand">ZEST SUPPLEMENTS</p>
    <div class="halo"></div>
    <p class="category">• FOOD SUPPLEMENT •</p>
    <div class="title-pill"></div>
    <h2 class="title title--top">PROTEIN</h2>
    <p class="title title--bottom">POWDER</p>
    <p class="flavour">STRAWBERRIES &amp; CREAM</p>
    <div class="flavour-dot"></div>
    <p class="weight">500G</p>
  </article>

  <article class="pouch pouch--vanilla">
    <div class="pouch__pattern" role="img" aria-label="Black pouch face with fine radiating line pattern"></div>
    <div class="pouch__seal"></div>
    <div class="pouch__tear"></div>
    <p class="brand">ZEST SUPPLEMENTS</p>
    <div class="halo"></div>
    <p class="category">• FOOD SUPPLEMENT •</p>
    <div class="title-pill"></div>
    <h2 class="title title--top">PROTEIN</h2>
    <p class="title title--bottom">POWDER</p>
    <p class="flavour">VANILLA ICE CREAM</p>
    <div class="flavour-dot"></div>
    <p class="weight">500G</p>
  </article>

</main>
</body>
</html>
```